The Timber Loft

We need a business card design for our wardrobe company.
Please visit our website www.zorvelcabinets.com to get an idea of who we are.

```html
<!DOCTYPE html>
<html lang="en">
<head>
<meta charset="utf-8">
<title>The Timber Loft – Business Card</title>
<link href="https://fonts.googleapis.com/css2?family=Roboto:wght@400;500;700;900&display=swap" rel="stylesheet">
<style>
  :root {
    --backdrop: #c9b89c;
    --charcoal: #1f1f1f;
    --charcoal-light: #3a3a3a;
    --gold: #a8874f;
    --gold-dark: #7d6235;
    --gold-light: #c4a56c;
    --paper: #ffffff;
    --paper-shade: #ecebe8;
    --ink: #2a2a2a;
    --ink-soft: #4a4a4a;
  }
  * { margin: 0; padding: 0; box-sizing: border-box; }
  html, body { width: 900px; height: 1200px; overflow: hidden; }
  body {
    background: var(--backdrop);
    font-family: "Roboto", Arial, sans-serif;
    color: var(--ink);
    position: relative;
  }
  .card {
    position: absolute;
    left: 60px;
    width: 780px;
    height: 460px;
    border-radius: 22px;
    overflow: hidden;
    background: linear-gradient(180deg, var(--paper) 60%, var(--paper-shade));
    box-shadow: 0 6px 18px rgba(0,0,0,0.35);
  }
  .card--front { top: 95px; }
  .card--back { top: 650px; }

  .card__header {
    position: absolute; left: 0; top: 0; width: 100%; height: 150px;
    background: linear-gradient(180deg, var(--charcoal-light), var(--charcoal));
  }
  .brand {
    position: absolute; left: 26px; top: 30px;
    display: flex; align-items: center; gap: 22px;
  }
  .brand__square {
    width: 92px; height: 86px;
    border: 3px solid var(--paper);
    border-radius: 4px;
  }
  .brand__name {
    font-size: 21px; font-weight: 500; color: var(--paper);
    text-transform: uppercase; letter-spacing: 0.5px;
  }
  .brand__tagline {
    margin-top: 10px; font-size: 21px; color: var(--paper);
  }
  .header__panel {
    position: absolute; right: 30px; top: 18px;
    width: 230px; height: 114px;
    border: 2px solid rgba(255,255,255,0.08);
    background: linear-gradient(135deg, rgba(255,255,255,0.06), rgba(255,255,255,0.01));
  }

  .card__statement {
    position: absolute; left: 0; top: 150px; width: 100%; height: 38px;
    background: linear-gradient(180deg, var(--gold-light), var(--gold));
    color: var(--paper); font-size: 17px;
    display: flex; align-items: center; padding-left: 34px;
    white-space: nowrap;
  }

  .person {
    position: absolute; left: 34px; top: 222px; right: 34px;
    padding-bottom: 14px;
    border-bottom: 3px solid var(--gold);
    display: flex; align-items: baseline; gap: 14px;
  }
  .person__name { font-size: 40px; font-weight: 900; color: var(--ink); letter-spacing: 0.5px; }
  .person__role { font-size: 17px; font-weight: 700; color: var(--gold); text-transform: uppercase; }

  .contacts {
    position: absolute; left: 34px; top: 302px;
    list-style: none;
  }
  .contacts li {
    display: flex; align-items: center; gap: 12px;
    font-size: 17px; color: var(--ink-soft); height: 30px;
  }
  .contacts svg { width: 20px; height: 20px; flex: none; }

  .address {
    position: absolute; right: 34px; top: 306px;
    text-align: right; font-size: 18px; line-height: 30px; color: var(--ink);
    font-style: normal;
  }

  .card__footer {
    position: absolute; left: 0; bottom: 0; width: 100%; height: 50px;
    background: linear-gradient(180deg, var(--gold), var(--gold-dark));
    display: flex; align-items: center; justify-content: space-between;
    padding: 0 30px 0 34px;
  }
  .footer__label { color: var(--paper); font-size: 17px; font-weight: 700; text-transform: uppercase; }
  .social { display: flex; gap: 8px; }
  .social span {
    width: 28px; height: 28px; border-radius: 50%;
    background: rgba(255,255,255,0.45);
  }
</style>
</head>
<body>

<article class="card card--front">
  <header class="card__header">
    <div class="brand">
      <div class="brand__square"></div>
      <div>
        <div class="brand__name">The Timber Loft</div>
        <div class="brand__tagline">Built to Fit Your Space</div>
      </div>
    </div>
    <div class="header__panel" role="img" aria-label="Faint decorative brand panel"></div>
  </header>
  <div class="card__statement">We design and fit made-to-measure storage for homes across the city.</div>
  <div class="person">
    <span class="person__name">DANIEL HART</span>
    <span class="person__role">Managing Director</span>
  </div>
  <ul class="contacts">
    <li><svg viewBox="0 0 20 20"><circle cx="10" cy="10" r="10" fill="#a8874f"/><path d="M7 5l2 2.5-1.2 1.4a6 6 0 0 0 3.3 3.3l1.4-1.2L15 13l-1 2c-4.5 0-9-4.5-9-9z" fill="#fff"/></svg>0207 555 0148</li>
    <li><svg viewBox="0 0 20 20"><circle cx="10" cy="10" r="10" fill="#a8874f"/><rect x="5" y="6.5" width="10" height="7" fill="none" stroke="#fff" stroke-width="1.4"/><path d="M5 6.5l5 4 5-4" fill="none" stroke="#fff" stroke-width="1.4"/></svg>info@zorvelcabinets.com</li>
    <li><svg viewBox="0 0 20 20"><circle cx="10" cy="10" r="10" fill="#a8874f"/><circle cx="10" cy="10" r="5" fill="none" stroke="#fff" stroke-width="1.4"/><path d="M5 10h10M10 5v10" stroke="#fff" stroke-width="1.2"/></svg>www.zorvelcabinets.com</li>
  </ul>
  <address class="address">Alder House, 42 Marlow Street<br>London N1 7QE</address>
  <footer class="card__footer">
    <span class="footer__label">Find us on</span>
    <div class="social"><span></span><span></span><span></span><span></span></div>
  </footer>
</article>

<article class="card card--back">
  <header class="card__header">
    <div class="brand">
      <div class="brand__square"></div>
      <div>
        <div class="brand__name">The Timber Loft</div>
        <div class="brand__tagline">Built to Fit Your Space</div>
      </div>
    </div>
    <div class="header__panel" role="img" aria-label="Faint decorative brand panel"></div>
  </header>
  <div class="card__statement">We design and fit made-to-measure storage for homes across the city.</div>
  <div class="person">
    <span class="person__name">DANIEL HART</span>
    <span class="person__role">Managing Director</span>
  </div>
  <ul class="contacts">
    <li><svg viewBox="0 0 20 20"><circle cx="10" cy="10" r="10" fill="#a8874f"/><path d="M7 5l2 2.5-1.2 1.4a6 6 0 0 0 3.3 3.3l1.4-1.2L15 13l-1 2c-4.5 0-9-4.5-9-9z" fill="#fff"/></svg>0207 555 0148</li>
    <li><svg viewBox="0 0 20 20"><circle cx="10" cy="10" r="10" fill="#a8874f"/><rect x="5" y="6.5" width="10" height="7" fill="none" stroke="#fff" stroke-width="1.4"/><path d="M5 6.5l5 4 5-4" fill="none" stroke="#fff" stroke-width="1.4"/></svg>info@zorvelcabinets.com</li>
    <li><svg viewBox="0 0 20 20"><circle cx="10" cy="10" r="10" fill="#a8874f"/><circle cx="10" cy="10" r="5" fill="none" stroke="#fff" stroke-width="1.4"/><path d="M5 10h10M10 5v10" stroke="#fff" stroke-width="1.2"/></svg>www.zorvelcabinets.com</li>
  </ul>
  <address class="address">Alder House, 42 Marlow Street<br>London N1 7QE</address>
  <footer class="card__footer">
    <span class="footer__label">Find us on</span>
    <div class="social"><span></span><span></span><span></span><span></span></div>
  </footer>
</article>

</body>
</html>
```